Company Website

Our company teaches Corvane Accredited Medic certification. Our company name is Harbrook Training Group. (logo is in the files). We have a current website that needs an overhaul (www.harbrooktraininggroup.com). This website needs to able to be used on wordpress. We need a website that has a good flow and design, have a page that has our instructor bio’s, a page on our class information, prerequisites, and how many seats are left in the class, a page that will accept payments and layout our cost. Be able to expand as our company expands to other classes (CPR ETC.)

Target Market(s)

People that want to take an EMT class

Coding

Coded - Design and coding required

Number of Pages Required

3 page

Requirements
Must have
• A page explaining who we are, a page of the services we offer with the ability to pay using Quidlo or some external source, and a page about who the instructors are.
Nice to have
• Good flow, easy to change as the Business grows

```html
<!DOCTYPE html>
<html lang="en">
<head>
<meta charset="utf-8">
<title>Harbrook Training Group</title>
<link href="https://fonts.googleapis.com/css2?family=Red+Hat+Display:wght@400;500;700&family=Mulish:wght@400;600;700&display=swap" rel="stylesheet">
<style>
:root{
  --navy:#1b2230;
  --navy-deep:#141a25;
  --red:#d0103a;
  --red-dark:#9e0c2e;
  --white:#ffffff;
  --text:#5b5f66;
  --heading:#1e2330;
  --muted:#8b9099;
}
*{margin:0;padding:0;box-sizing:border-box}
html,body{width:1200px;height:3346px;overflow:hidden}
body{position:relative;background:var(--white);font-family:"Mulish",sans-serif;color:var(--text)}
.abs{position:absolute}
h1,h2,h3,h4{font-family:"Red Hat Display",sans-serif;font-weight:500}

/* header */
.site-header{left:0;top:0;width:1200px;height:78px;background:var(--navy);z-index:5}
.brand{display:flex;align-items:center;gap:10px}
.brand-dot{width:22px;height:22px;border-radius:50%;background:var(--red)}
.brand-name{font-family:"Red Hat Display",sans-serif;font-weight:700;color:var(--red);font-size:20px;letter-spacing:.3px}
.site-header .brand{left:60px;top:24px}
.main-nav{left:377px;top:30px;display:flex;gap:24px}
.main-nav a{color:var(--white);font-size:12px;text-decoration:none;letter-spacing:.3px}
.call{left:910px;top:14px;display:flex;align-items:center;gap:14px}
.call-icon{width:48px;height:48px;border-radius:50%;background:var(--red);display:flex;align-items:center;justify-content:center}
.call small{display:block;color:var(--red);font-size:12px}
.call strong{display:block;color:var(--white);font-family:"Red Hat Display",sans-serif;font-weight:400;font-size:25px;line-height:1}

/* hero */
.hero{left:0;top:0;width:1200px;height:745px;background:radial-gradient(ellipse at 55% 45%,#3b4a66 0%,#1d2a42 45%,#0c1322 100%)}
.seats{left:0;width:1200px;top:224px;text-align:center;color:var(--red);font-family:"Red Hat Display",sans-serif;font-size:24px;font-weight:500}
.hero-title{left:0;width:1200px;top:252px;text-align:center;color:var(--white);font-size:62px;font-weight:700}
.hero-lead{left:190px;width:820px;top:338px;text-align:center;color:var(--white);font-size:15px;font-weight:700;line-height:30px}
.countdown{left:344px;top:428px;display:flex;gap:16px}
.count{width:117px;height:92px;background:rgba(20,26,38,.75);text-align:center;color:var(--white)}
.count b{display:block;font-family:"Red Hat Display",sans-serif;font-size:42px;font-weight:500;line-height:58px;padding-top:6px}
.count span{font-size:12px;font-weight:700}

/* class info */
.section-title{font-size:35px;color:var(--heading)}
.section-title em{font-style:normal;color:var(--red)}
.class-title{left:109px;top:818px}
.title-rule{height:4px;width:92px;background:var(--red);border-radius:2px}
.class-rule{left:109px;top:866px}
.class-copy{left:109px;top:902px;width:450px;font-size:15px;line-height:30px;color:var(--text)}
.btn-dark{left:109px;top:1201px;width:182px;height:54px;border-radius:22px 0 0 0;background:linear-gradient(90deg,var(--navy) 30%,var(--red));color:var(--white);font-size:15px;font-weight:600;display:flex;align-items:center;justify-content:center}
.photo{position:absolute}

/* instructors */
.dark-band{left:0;top:1350px}
.band-title{left:0;width:1200px;top:1472px;text-align:center;color:var(--white);font-size:35px}
.band-rule{left:555px;top:1521px;width:90px;height:4px;background:var(--white)}
.bio-photo{width:188px;height:188px;border-radius:50%;background:radial-gradient(circle at 50% 40%,#cfcac5,#7d7570 70%,#3a3533)}
.bio-name{color:var(--red);font-family:"Red Hat Display",sans-serif;font-size:17px;font-weight:500;letter-spacing:.3px}
.bio-text{color:var(--white);font-size:13px;line-height:30px;width:240px;margin-top:6px}
.bio-social{display:flex;gap:6px;margin-top:6px}
.bio-social i{width:12px;height:12px;border-radius:50%;background:var(--red);display:block}

/* pricing */
.pricing-title{left:0;width:1200px;top:2222px;text-align:center}
.pricing-rule{left:555px;top:2271px}
.plan{position:absolute;border-radius:50%;border:10px solid var(--red);background:var(--white);text-align:center;box-shadow:0 6px 20px rgba(0,0,0,.2)}
.plan h4{font-size:17px;font-weight:700;color:var(--heading)}
.plan .price{font-family:"Red Hat Display",sans-serif;font-size:44px;font-weight:700;color:var(--heading);line-height:1}
.plan .price sup{font-size:24px;font-weight:500;vertical-align:22px;margin-left:4px}
.plan p{font-size:15px;line-height:26px;color:var(--muted);margin:12px auto 0;width:190px}
.plan .pill{display:inline-block;margin-top:16px;border:1px solid var(--red);border-radius:22px;padding:8px 20px;color:var(--red);font-size:16px;background:var(--white)}
.plan.featured{background:radial-gradient(circle at 80% 55%,var(--red),var(--red-dark) 40%,#2a1a28 100%)}
.plan.featured h4,.plan.featured .price,.plan.featured p{color:var(--white)}

/* footer */
.footer-band{left:0;top:2730px}
.mail-title{left:0;width:1200px;top:2830px;text-align:center;color:var(--white);font-size:35px;font-weight:700}
.mail-lead{left:0;width:1200px;top:2893px;text-align:center;color:var(--white);font-size:12px}
.mail-form{left:279px;top:2935px;width:640px;height:52px;border-radius:26px;background:var(--white);border:2px solid var(--red)}
.mail-form span{position:absolute;left:46px;top:17px;font-size:12px;color:var(--muted)}
.mail-form b{position:absolute;right:2px;top:2px;width:138px;height:44px;border-radius:22px;background:linear-gradient(90deg,var(--navy),var(--red));color:var(--white);font-weight:400;font-size:16px;display:flex;align-items:center;justify-content:center}
.rule-line{height:1px;background:#3a4254}
.footer-brand{left:106px;top:3080px}
.footer-social{left:126px;top:3130px;display:flex;gap:15px}
.footer-social i{width:32px;height:32px;border-radius:50%;background:var(--white);display:block}
.pay-badges{left:124px;top:3192px;display:flex;gap:6px}
.pay-badges i{width:41px;height:26px;border-radius:3px;background:var(--white);display:block}
.footer-col h4{color:var(--white);font-size:16px;font-weight:700;margin-bottom:6px}
.footer-col li{list-style:none;color:var(--white);font-size:17px;line-height:30px}
.footer-col li::before{content:"\00BB";margin-right:8px}
.contact-row{display:flex;gap:12px;color:var(--white);font-size:17px;line-height:30px;margin-bottom:12px}
.contact-row svg{flex:none;margin-top:8px}
.copyright{left:0;width:1200px;top:3270px;text-align:center;color:var(--white);font-size:13px}
</style>
</head>
<body>

<section class="hero abs" role="img" aria-label="Ambulance speeding through a lit tunnel at night"></section>
<svg class="abs" style="left:0;top:620px" width="1200" height="130" viewBox="0 0 1200 130" aria-hidden="true">
  <path d="M0 55 C160 130 420 125 700 85 S1080 30 1200 35 L1200 130 L0 130Z" fill="#fff"/>
  <path d="M0 55 C160 130 420 125 700 85 S1080 30 1200 35" fill="none" stroke="#d0103a" stroke-width="6"/>
</svg>

<header class="site-header abs">
  <div class="brand abs"><span class="brand-dot"></span><span class="brand-name">Harbrook Training Group</span></div>
  <nav class="main-nav abs">
    <a href="#">HOME</a><a href="#">OUR INSTRUCTOR</a><a href="#">OUR CLASS</a><a href="#">PRICING</a><a href="#">CONTACT US</a>
  </nav>
  <div class="call abs">
    <span class="call-icon"><svg width="18" height="18" viewBox="0 0 24 24"><path fill="#fff" d="M6.6 10.8a15 15 0 0 0 6.6 6.6l2.2-2.2c.3-.3.7-.4 1-.2 1.1.4 2.3.6 3.6.6.6 0 1 .4 1 1V20c0 .6-.4 1-1 1A17 17 0 0 1 3 4c0-.6.4-1 1-1h3.5c.6 0 1 .4 1 1 0 1.3.2 2.5.6 3.6.1.3 0 .7-.2 1z"/></svg></span>
    <div><small>Call Us Today</small><strong>+ 123 456 7890</strong></div>
  </div>
</header>

<p class="seats abs">15 Seats Left!!</p>
<h1 class="hero-title abs">Your Journey Begins</h1>
<p class="hero-lead abs">Always find yourself watching the ambulance or fire truck go by and wish you could do that? Do you desire to help the community around you? Let our initial EMT course set you in the career path you desire.</p>
<div class="countdown abs">
  <div class="count"><b>15</b><span>DAYS</span></div>
  <div class="count"><b>5</b><span>HOURS</span></div>
  <div class="count"><b>10</b><span>MINUTES</span></div>
  <div class="count"><b>56</b><span>SECONDS</span></div>
</div>

<h2 class="section-title class-title abs">Our Class <em>Information</em></h2>
<div class="title-rule class-rule abs"></div>
<p class="class-copy abs">Sed ut perspiciatis unde omnis iste natus error sit voluptatem accusantium doloremque laudantium, totam rem aperiam, eaque ipsa quae ab illo inventore veritatis et quasi architecto beatae vitae dicta sunt explicabo. Nemo enim ipsam voluptatem quia voluptas sit aspernatur aut odit aut fugit, sed quia conse quuntur magni dolores eos qui ratione voluptatem sequinesci unt. Neque porro quisquam est, qui dolorem ipsum quia dolor sit amet, consectetur, adipisci velit, sed quia non numquam eius modi tempora incidunt ut labore.</p>
<div class="btn-dark abs">View other classes</div>

<div class="photo" style="left:604px;top:832px;width:240px;height:215px;background:linear-gradient(135deg,#0d0d1a,#5a1020 55%,#c0304a)" role="img" aria-label="Responder walking toward an emergency vehicle at night"></div>
<div class="photo" style="left:604px;top:1052px;width:240px;height:214px;background:linear-gradient(135deg,#0f2a20,#7a1020 50%,#d23a3a)" role="img" aria-label="Fire rescue truck in motion at night"></div>
<div class="photo" style="left:849px;top:791px;width:241px;height:214px;background:linear-gradient(135deg,#dcdcdc,#6a6a6a 60%,#2a2a2a)" role="img" aria-label="Black and white photo of parked ambulances"></div>
<div class="photo" style="left:849px;top:1009px;width:241px;height:214px;background:linear-gradient(135deg,#2a3550,#5c6a88 45%,#1a1d24)" role="img" aria-label="Police car light bar close up"></div>

<svg class="dark-band abs" width="1200" height="790" viewBox="0 0 1200 790" aria-hidden="true">
  <path d="M0 80 C300 120 620 0 975 5 S1160 40 1200 60 L1200 693 C1000 690 600 740 320 785 C180 800 60 760 0 728Z" fill="#1b2230"/>
  <path d="M0 80 C300 120 620 0 975 5 S1160 40 1200 60" fill="none" stroke="#d0103a" stroke-width="6"/>
  <path d="M1200 693 C1000 690 600 740 320 785 C180 800 60 760 0 728" fill="none" stroke="#d0103a" stroke-width="6"/>
</svg>
<h2 class="band-title abs">Our Instructor Bio’s</h2>
<div class="band-rule abs"></div>

<div class="bio-photo abs" style="left:100px;top:1553px" role="img" aria-label="Portrait of instructor Callum Wexford"></div>
<div class="abs" style="left:312px;top:1574px">
  <h3 class="bio-name">CALLUM WEXFORD</h3>
  <p class="bio-text">Sed ut perspiciatis unde omnis iste natus error sit voluptatem</p>
  <div class="bio-social"><i></i><i></i><i></i></div>
</div>
<div class="bio-photo abs" style="left:608px;top:1553px" role="img" aria-label="Portrait of instructor Marisol Okafor-Lind"></div>
<div class="abs" style="left:823px;top:1590px">
  <h3 class="bio-name">MARISOL OKAFOR-LIND</h3>
  <p class="bio-text">Sed ut perspiciatis unde omnis iste natus error sit voluptatem</p>
  <div class="bio-social"><i></i><i></i><i></i></div>
</div>
<div class="bio-photo abs" style="left:100px;top:1810px" role="img" aria-label="Portrait of instructor Teodora V. Amsel"></div>
<div class="abs" style="left:312px;top:1842px">
  <h3 class="bio-name">TEODORA V. AMSEL</h3>
  <p class="bio-text">Sed ut perspiciatis unde omnis iste natus error sit voluptatem</p>
  <div class="bio-social"><i></i><i></i><i></i></div>
</div>
<div class="bio-photo abs" style="left:608px;top:1810px" role="img" aria-label="Portrait of instructor Rhys Delacourt"></div>
<div class="abs" style="left:823px;top:1842px">
  <h3 class="bio-name">RHYS DELACOURT</h3>
  <p class="bio-text">Sed ut perspiciatis unde omnis iste natus error sit voluptatem</p>
  <div class="bio-social"><i></i><i></i><i></i></div>
</div>

<h2 class="section-title pricing-title abs">Our Pricing <em>Plans</em></h2>
<div class="title-rule pricing-rule abs"></div>

<div class="plan" style="left:143px;top:2364px;width:278px;height:278px;padding-top:36px">
  <h4>Standard</h4>
  <div class="price">5.7<sup>$/Mon</sup></div>
  <p>Sed ut perspiciatis unde omnis iste natus error voluptatem</p>
  <span class="pill">Learn More</span>
</div>
<div class="plan featured" style="left:461px;top:2322px;width:278px;height:278px;padding-top:36px">
  <h4>Commercial</h4>
  <div class="price">3.9<sup>$/Mon</sup></div>
  <p>Sed ut perspiciatis unde omnis iste natus error voluptatem</p>
  <span class="pill">Learn More</span>
</div>
<div class="plan" style="left:779px;top:2364px;width:278px;height:278px;padding-top:36px">
  <h4>Personal</h4>
  <div class="price">6.8<sup>$/Mon</sup></div>
  <p>Sed ut perspiciatis unde omnis iste natus error voluptatem</p>
  <span class="pill">Learn More</span>
</div>

<svg class="footer-band abs" width="1200" height="616" viewBox="0 0 1200 616" aria-hidden="true">
  <path d="M0 80 C250 95 500 60 800 40 S1120 0 1200 5 L1200 616 L0 616Z" fill="#1b2230"/>
  <path d="M0 80 C250 95 500 60 800 40 S1120 0 1200 5" fill="none" stroke="#d0103a" stroke-width="6"/>
</svg>
<h2 class="mail-title abs">Join Our mailing List</h2>
<p class="mail-lead abs">Lorem ipsum dolor sit amet, consectetur adipiscing elit, sed do eiusmod tempor</p>
<div class="mail-form abs"><span>Enter Email Here</span><b>SUBMIT</b></div>
<div class="rule-line abs" style="left:112px;top:3019px;width:976px"></div>

<div class="brand footer-brand abs"><span class="brand-dot"></span><span class="brand-name">Harbrook Training Group</span></div>
<div class="footer-social abs"><i></i><i></i><i></i><i></i></div>
<div class="pay-badges abs"><i></i><i></i><i></i><i></i></div>

<div class="footer-col abs" style="left:375px;top:3058px">
  <h4>QUICK LINKS</h4>
  <ul><li>Home</li><li>Our Instructor</li><li>Our Class</li><li>Pricing</li><li>Contact Us</li></ul>
</div>
<div class="footer-col abs" style="left:564px;top:3058px">
  <h4>LEGAL</h4>
  <ul><li>Terms of Use</li><li>Privacy Policy</li><li>Contact Us</li><li>FAQ</li></ul>
</div>
<div class="footer-col abs" style="left:795px;top:3058px;width:300px">
  <h4>CONTACT US</h4>
  <div class="contact-row"><svg width="12" height="16" viewBox="0 0 12 16"><path fill="#fff" d="M6 0a6 6 0 0 0-6 6c0 4.5 6 10 6 10s6-5.5 6-10a6 6 0 0 0-6-6zm0 8.5A2.5 2.5 0 1 1 6 3.5a2.5 2.5 0 0 1 0 5z"/></svg><span>123 Lorem ipsum dolor sit amet, consectetur adipiscing elit</span></div>
  <div class="contact-row"><svg width="14" height="14" viewBox="0 0 24 24"><path fill="#fff" d="M6.6 10.8a15 15 0 0 0 6.6 6.6l2.2-2.2c.3-.3.7-.4 1-.2 1.1.4 2.3.6 3.6.6.6 0 1 .4 1 1V20c0 .6-.4 1-1 1A17 17 0 0 1 3 4c0-.6.4-1 1-1h3.5c.6 0 1 .4 1 1 0 1.3.2 2.5.6 3.6.1.3 0 .7-.2 1z"/></svg><span>+ 123 456 7890</span></div>
  <div class="contact-row"><svg width="16" height="12" viewBox="0 0 16 12"><path fill="#fff" d="M0 0h16v1.5L8 7 0 1.5zM0 3.3l8 5.4 8-5.4V12H0z"/></svg><span>info@harbrooktraininggroup.com</span></div>
</div>

<div class="rule-line abs" style="left:75px;top:3248px;width:1050px"></div>
<p class="copyright abs">© Copyrights 2021 Harbrook Training Group &nbsp; | &nbsp; All Rights Reserved</p>

</body>
</html>
```